Design for an Orbit and Nimbus app managing shopping list

The app allows you to keep manage shopping lists, each shopping list being made of items to buy...
We need a design for the 3 screens of the app:
a) global view showing list of (shopping) list
b) form enabling to edit the name of a (shopping) list
c) detailed view listing the contents/items of a (shopping) list
d) 1 text page [not illustrated]
2 "alerts" items are also to be designed: confirm and error pop ups.
No specific guidelines, nor logo or whatever.
It will be a free app distributed on Orbit and Androïd.
We just want to make it looking nice & very usable for end users.

```html
<!DOCTYPE html>
<html lang="en">
<head>
<meta charset="utf-8">
<title>Shopping Lists – App Design</title>
<link rel="stylesheet" href="https://fonts.googleapis.com/css2?family=Montserrat:ital,wght@0,400;0,500;0,600;0,700;0,800;1,400;1,500&display=swap">
<style>
  :root {
    --bg-top: #0f1a30;
    --bg-bottom: #176a8a;
    --accent-line: #1fc6d0;
    --white: #ffffff;
    --app-header: #2c3649;
    --app-header-light: #36425a;
    --app-teal: #12c3cc;
    --app-teal-light: #0fd0d8;
    --card-text: #2f3445;
    --card-muted: #9aa0ab;
    --card-border: #eceef1;
    --dot-red: #c6283a;
    --dot-orange: #e08a1e;
    --dot-green: #2a8a2e;
    --dot-blue: #3fb3f2;
    --dot-purple: #d37ff0;
    --overlay: rgba(40, 40, 40, 0.86);
    --banner: rgba(0, 0, 0, 0.92);
    --banner-text: #ff2a7f;
  }
  * { box-sizing: border-box; margin: 0; padding: 0; }
  html, body { width: 1200px; height: 1200px; overflow: hidden; }
  body {
    font-family: "Montserrat", sans-serif;
    background: linear-gradient(160deg, var(--bg-top) 0%, #12304a 45%, var(--bg-bottom) 100%);
    position: relative;
  }
  .project-title {
    position: absolute; left: 66px; top: 74px;
    padding-left: 20px;
    border-left: 3px solid var(--accent-line);
    color: var(--white);
  }
  .project-title h1 { font-size: 34px; font-weight: 700; line-height: 1.1; }
  .project-title p { font-size: 21px; font-weight: 400; margin-top: 12px; }

  .app-screen {
    position: absolute; left: 390px; top: 170px;
    width: 420px; height: 684px;
    background: var(--white);
    overflow: hidden;
    box-shadow: 0 30px 70px rgba(0,0,0,0.35);
  }
  .app-header {
    height: 58px;
    background: linear-gradient(90deg, var(--app-header) 72%, var(--app-header-light) 72%);
    display: flex; align-items: center; gap: 14px; padding-left: 22px;
    color: var(--white);
  }
  .app-name { font-size: 20px; font-weight: 700; letter-spacing: 0.5px; }
  .section-bar {
    height: 76px;
    background: linear-gradient(90deg, var(--app-teal) 68%, var(--app-teal-light) 68%);
    display: flex; align-items: center; justify-content: space-between;
    padding: 0 22px;
    color: var(--white);
  }
  .section-bar h2 { font-size: 30px; font-weight: 400; }
  .section-actions { display: flex; gap: 18px; }

  .group-grid {
    display: grid; grid-template-columns: 1fr 1fr;
    grid-auto-rows: 196px;
  }
  .group-card {
    border-right: 1px solid var(--card-border);
    border-bottom: 1px solid var(--card-border);
    padding: 34px 12px 0;
    text-align: center;
    color: var(--card-text);
  }
  .group-card:nth-child(2n) { border-right: none; }
  .group-name { font-size: 20px; font-weight: 500; font-style: italic; line-height: 1.2; }
  .group-count { font-size: 11px; font-style: italic; color: var(--card-muted); margin-top: 16px; letter-spacing: 0.5px; }
  .group-dot { width: 11px; height: 11px; border-radius: 50%; margin: 16px auto 0; }
  .dot-red { background: var(--dot-red); }
  .dot-orange { background: var(--dot-orange); }
  .dot-green { background: var(--dot-green); }
  .dot-blue { background: var(--dot-blue); }
  .dot-purple { background: var(--dot-purple); }

  .play-button {
    position: absolute; left: 432px; top: 432px;
    width: 336px; height: 336px; border-radius: 50%;
    background: var(--overlay);
  }
  .play-button svg { position: absolute; left: 0; top: 0; }

  .watch-banner {
    position: absolute; left: 149px; top: 854px;
    width: 902px; height: 168px;
    background: var(--banner);
    display: flex; align-items: center; justify-content: center;
  }
  .watch-banner span {
    color: var(--banner-text);
    font-size: 58px; font-weight: 700; letter-spacing: 0.5px;
    white-space: nowrap;
  }
</style>
</head>
<body>
  <header class="project-title">
    <h1>Shopping Lists</h1>
    <p>Design for Orbit and Nimbus</p>
  </header>

  <main class="app-screen">
    <div class="app-header">
      <svg width="26" height="20" viewBox="0 0 26 20" aria-hidden="true">
        <g stroke="#fff" stroke-width="2.4" stroke-linecap="round">
          <line x1="2" y1="3" x2="24" y2="3"/>
          <line x1="2" y1="10" x2="20" y2="10"/>
          <line x1="2" y1="17" x2="24" y2="17"/>
        </g>
      </svg>
      <span class="app-name">CARTLY</span>
    </div>
    <div class="section-bar">
      <h2>My Groups</h2>
      <div class="section-actions">
        <svg width="26" height="26" viewBox="0 0 26 26" aria-label="Edit">
          <line x1="4" y1="22" x2="22" y2="4" stroke="#fff" stroke-width="3" stroke-linecap="round"/>
        </svg>
        <svg width="26" height="26" viewBox="0 0 26 26" aria-label="Add">
          <g stroke="#fff" stroke-width="2.6" stroke-linecap="round">
            <line x1="13" y1="2" x2="13" y2="24"/><line x1="2" y1="13" x2="24" y2="13"/>
          </g>
        </svg>
      </div>
    </div>
    <section class="group-grid">
      <article class="group-card"><h3 class="group-name">Food</h3><p class="group-count">5 ITEMS</p><div class="group-dot dot-red"></div></article>
      <article class="group-card"><h3 class="group-name">Shop at Norvik</h3><p class="group-count">3 ITEMS</p><div class="group-dot dot-orange"></div></article>
      <article class="group-card"><h3 class="group-name">Book</h3><p class="group-count">4 ITEMS</p><div class="group-dot dot-orange"></div></article>
      <article class="group-card"><h3 class="group-name">Home<br>Improvement</h3><p class="group-count">7 ITEMS</p><div class="group-dot dot-green"></div></article>
      <article class="group-card"><h3 class="group-name">Birthday<br>Party</h3><p class="group-count">9 ITEMS</p><div class="group-dot dot-blue"></div></article>
      <article class="group-card"><h3 class="group-name">Clothing</h3><p class="group-count">5 ITEMS</p><div class="group-dot dot-purple"></div></article>
    </section>
  </main>

  <div class="play-button" aria-label="Play video">
    <svg width="336" height="336" viewBox="0 0 336 336" aria-hidden="true">
      <polygon points="110,80 110,256 254,168" fill="#fff"/>
    </svg>
  </div>

  <div class="watch-banner"><span>WATCH ON CLIPSTREAM</span></div>
</body>
</html>
```